Vendrafel - Joint website

Recently, three of our organizations: Moriwell, PLIMB, and Tavolin have united to work on a single project - Advanced Recycling of plastic waste via technology - Vendrafel. For this united project, we need a new design of the website under the name of Vendrafel which would feature the three companies.

Target Market(s)

Suppliers, consumers, and consumer brand companies within the Petrochemicals industry

Coding

Coded - Design and coding required

Number of Pages Required

1 page

Font styles to use
Other font styles liked:
• Lato

Requirements
Must have
• A clear image of how the Vendrafel technology works/Sustainable aspect elaborated. The video on the home page featuring the three company representatives: https://www.clipvault-example.net/watch?v=qZTW8mLPa4J&channel=fennoraBrisk
Nice to have
• Make use of icons, explained with some text for the technology. / make clear which role every company has within this initiative. / Picture of the first truck, with the banner of the three companies. / short video of the factory and technology.
Should not have
• A divided theme, it must be clear that it is a collaborated initiative, and that we all work together within our own expertise. / No cliché sustainability pictures, that aren’t relevant to the product.

```html
<!DOCTYPE html>
<html lang="en">
<head>
<meta charset="utf-8">
<title>Vendrafel – Advanced Recycling</title>
<link href="https://fonts.googleapis.com/css2?family=Lato:wght@300;400;700;900&display=swap" rel="stylesheet">
<style>
:root{
  --orange:#e8652a;
  --amber:#f2a324;
  --green:#1f8c46;
  --ink:#262626;
  --text:#4a4a4a;
  --muted:#7a7a7a;
  --page:#eeeeef;
  --footer:#353535;
  --line:#d9d9d9;
}
*{box-sizing:border-box;margin:0;padding:0}
html,body{width:1200px;height:4743px;overflow:hidden}
body{font-family:'Lato',sans-serif;color:var(--text);background:var(--page);position:relative}
.canvas{position:relative;width:1200px;height:4743px;overflow:hidden;
  background:linear-gradient(180deg,#ececed 0,#f3f3f4 900px,#ffffff 1300px,#ffffff 1650px)}
.abs{position:absolute}
.wordmark{font-family:'Lato',sans-serif;font-weight:700;color:#7b7b7b;letter-spacing:1px;display:flex;align-items:center;gap:10px}
.wordmark .dot{width:12px;height:12px;background:var(--orange)}

/* header */
.brand{left:147px;top:48px;font-size:44px}
.nav{left:449px;top:48px;width:598px;height:48px;background:#fff;border-radius:4px;display:flex;align-items:center;justify-content:space-around;font-size:14px;color:var(--ink);box-shadow:0 2px 8px rgba(0,0,0,.06)}
.support{left:880px;top:16px;font-size:12px;color:#fff;display:flex;gap:6px;align-items:center;z-index:3}

.hero-visual{left:560px;top:-180px;width:760px;height:790px;border-radius:50%;
  background:radial-gradient(circle at 45% 40%,#f2c94c 0,#d9a02a 28%,#7a6a4a 55%,#3d4a6a 80%);
  box-shadow:0 0 0 26px var(--amber) inset}
.hero-title{left:147px;top:244px;font-size:33px;font-weight:900;line-height:44px;color:#2f4f3f;letter-spacing:-.5px}
.hero-title span{color:var(--green)}
.hero-copy{left:147px;top:350px;width:350px;font-size:12.5px;line-height:22px;color:var(--text)}
.btn{display:inline-flex;align-items:center;justify-content:center;color:#fff;font-weight:700;border-radius:22px;
  background:linear-gradient(90deg,var(--orange),var(--amber))}
.hero-btn{left:147px;top:449px;width:160px;height:44px;font-size:16px;box-shadow:0 3px 10px rgba(232,101,42,.35)}

.statement{left:0;top:684px;width:1200px;text-align:center;font-size:22px;line-height:41px;color:var(--ink)}
.statement b{font-weight:700}

.video-main{left:200px;top:817px;width:805px;height:453px;background:#fff;border-radius:18px;padding:11px;box-shadow:0 10px 30px rgba(0,0,0,.18)}
.video-main .screen{width:100%;height:100%;border-radius:12px;background:linear-gradient(135deg,#2a2f35,#4a4e52 50%,#1d2024)}
.play{position:absolute;left:50%;top:50%;width:78px;height:78px;margin:-39px 0 0 -39px;border-radius:50%;background:#fff;display:flex;align-items:center;justify-content:center}
.play::after{content:"";border-left:22px solid #222;border-top:14px solid transparent;border-bottom:14px solid transparent;margin-left:6px}

.intro-title{left:0;top:1352px;width:1200px;text-align:center;font-size:32px;font-weight:700;line-height:44px;color:var(--ink)}
.intro-copy{left:250px;top:1458px;width:700px;text-align:center;font-size:12.5px;line-height:22px}

/* partners */
.partners-band{left:0;top:1650px;width:1200px;height:558px;background:linear-gradient(180deg,#2b2b2b,#4b4b45 55%,#8a8a7a)}
.partner{top:1785px;width:276px;height:326px;background:#fff;padding:38px 28px}
.partner .name{height:60px;display:flex;align-items:center;justify-content:center;margin-bottom:32px;
  font-size:36px;font-weight:700;color:var(--ink);letter-spacing:1px}
.partner p{font-size:12.5px;line-height:22.5px;color:var(--text)}

/* challenges */
.num{top:2282px;width:42px;height:92px;color:#fff;font-weight:700;font-size:19px;display:flex;align-items:flex-end;justify-content:center;padding-bottom:6px}
.num-orange{left:162px;background:linear-gradient(180deg,var(--orange),var(--amber))}
.num-green{left:723px;background:var(--green)}
.sec-title{top:2300px;font-size:33px;line-height:39px;font-weight:700;color:var(--ink)}
.challenge{left:162px;width:430px;display:flex;gap:20px;font-size:12.5px;line-height:21px}
.challenge svg{flex:0 0 36px}
.solution{left:723px;width:315px}
.solution h4{font-size:14px;color:var(--ink);font-weight:700;margin-bottom:14px}
.solution p{font-size:12.5px;line-height:21px}
.sol-btn{left:723px;top:2580px;width:130px;height:40px;border-radius:3px;font-size:13px}

.waste-bg{left:0;top:2630px;width:1200px;height:600px;background:linear-gradient(180deg,rgba(255,255,255,1) 0,#e3e5e8 35%,#cfd4da 70%,#e9ebee 100%)}
.video-small{left:313px;top:2703px;width:502px;height:337px;background:linear-gradient(135deg,#b9bdb8,#7d8a86 45%,#d9d6cf);box-shadow:0 8px 24px rgba(0,0,0,.2)}

.how-title{left:0;top:3228px;width:1200px;text-align:center;font-size:32px;font-weight:700;color:var(--ink)}
.step{font-size:14.5px;line-height:20px;color:var(--text)}
.step .brand-sm{font-size:26px;font-weight:700;color:#7b7b7b}

/* products */
.products{left:0;top:3772px;width:1200px;height:561px;background:linear-gradient(180deg,#e9ecef,#dde3e8 50%,#e6e9ec)}
.products-title{left:0;top:3825px;width:1200px;text-align:center;font-size:32px;font-weight:700;color:var(--ink)}
.product{top:3901px;width:372px;height:331px;background:#fff;padding:8px;box-shadow:0 6px 18px rgba(0,0,0,.08)}
.product .thumb{height:206px;display:flex;flex-direction:column;align-items:center;justify-content:center;gap:20px}
.product .thumb .wordmark{font-size:44px}
.product h5{font-size:18px;font-weight:400;color:var(--ink);margin:22px 12px 8px}
.product p{font-size:14px;line-height:20px;margin:0 12px;color:var(--text)}

/* footer */
.footer{left:0;top:4333px;width:1200px;height:410px;background:var(--footer);color:#e0e0e0}
.f-brand{left:162px;top:4400px;font-size:46px}
.f-h{font-size:15px;font-weight:700;color:#fff;letter-spacing:.3px}
.f-list{font-size:13px;line-height:28.5px;color:#dcdcdc;list-style:none}
.f-text{font-size:13px;line-height:20px;color:#dcdcdc}
.newsletter{left:709px;top:4508px;width:291px;height:44px;border:1px solid #888;border-radius:22px;display:flex;align-items:center;justify-content:space-between;padding:3px 3px 3px 28px;font-size:13px;color:#bbb}
.newsletter .btn{width:110px;height:36px;font-size:14px;font-weight:400;border-radius:18px}
.f-rule{left:162px;top:4655px;width:890px;height:1px;background:#555}
.social{left:162px;top:4676px;display:flex;gap:8px}
.social span{width:34px;height:34px;border-radius:50%;background:linear-gradient(135deg,var(--orange),var(--amber))}
.copy{left:700px;top:4686px;width:352px;text-align:right;font-size:12px;color:#ddd}
</style>
</head>
<body>
<div class="canvas">

  <!-- hero -->
  <div class="abs hero-visual" role="img" aria-label="Glass flask of amber recycled oil standing on shredded plastic waste"></div>
  <div class="abs support">
    <svg width="12" height="12" viewBox="0 0 12 12"><path d="M2 7v-1a4 4 0 0 1 8 0v1M2 7h2v3H2zM8 7h2v3H8z" fill="none" stroke="#fff" stroke-width="1.2"/></svg>
    hello@vendrafel-mail.net
  </div>
  <div class="abs brand wordmark">vendrafel<span class="dot"></span></div>
  <nav class="abs nav">
    <span>Home</span><span>Our partners</span><span>Technology</span><span>System and Operations</span><span>Contact</span>
  </nav>

  <h1 class="abs hero-title">CONVERTING WASTE TO<br><span>CIRCULAR RESOURCE!</span></h1>
  <p class="abs hero-copy">Lorem Ipsum is simply dummy text of the printing and typesetting industry. Lorem Ipsum has been the industry's standard dummy text ever since the 1500s</p>
  <a class="abs btn hero-btn">Learn More</a>

  <svg class="abs" style="left:0;top:960px" width="1200" height="700" viewBox="0 0 1200 700">
    <path d="M0 90 C220 20 420 0 600 60 C800 130 980 260 1200 220 L1200 700 L0 700 Z" fill="#fff"/>
  </svg>

  <p class="abs statement"><b>VENDRAFEL</b> will place systems for the liquefaction of plastic waste<br>at the locations where it is generated.</p>

  <div class="abs video-main">
    <div class="screen" role="img" aria-label="Video: the three company representatives in a studio discussion"></div>
    <span class="play"></span>
  </div>

  <h2 class="abs intro-title">Lorem Ipsum is simply dummy text of the<br>printing and typesetting.</h2>
  <p class="abs intro-copy">Lorem Ipsum is simply dummy text of the printing and typesetting industry. Lorem Ipsum has been the industry's standard dummy text ever since the 1500s, when an unknown printer took a galley of type and scrambled it to make a type specimen book. It has survived not only five centuries, but also the leap into electronic typesetting, remaining essentially unchanged. It was popularised in the 1960s with the release of Letraset sheets containing.</p>

  <!-- partners -->
  <div class="abs partners-band" role="img" aria-label="Dark photo of a plastic waste landfill"></div>
  <svg class="abs" style="left:0;top:1630px" width="1200" height="80" viewBox="0 0 1200 80">
    <defs><linearGradient id="og"><stop offset="0" stop-color="#e8652a"/><stop offset=".5" stop-color="#c0561f"/><stop offset="1" stop-color="#e8652a"/></linearGradient></defs>
    <path d="M0 62 C300 0 900 0 1200 62 L1200 24 C900 -8 300 -8 0 62 Z" fill="#fff"/>
    <path d="M0 62 C300 4 900 4 1200 62" fill="none" stroke="url(#og)" stroke-width="6"/>
  </svg>

  <div class="abs partner" style="left:162px">
    <div class="name">PLIMB</div>
    <p>PLIMB represents a diverse group of experts contributing to a sustainable future. We handle, trade, and explore commodities in energy, and renewables markets, with the aim to bring sustainability into a predominantly unsustainable market.</p>
  </div>
  <div class="abs partner" style="left:462px">
    <div class="name">MORIWELL</div>
    <p>MORIWELL specializes in lid films, rigid/flexible films and bags. Films are printed using flexographic, gravure and digital printing processes. Their aspiration is to find the optimal packaging solution for all kinds of products.</p>
  </div>
  <div class="abs partner" style="left:762px">
    <div class="name">TAVOLIN</div>
    <p>TAVOLIN represents a diverse group of experts contributing to a sustainable future. We handle, trade, and explore commodities in energy, and renewables markets, with the aim to bring sustainability into a predominantly unsustainable market.</p>
  </div>

  <!-- challenges / solution -->
  <div class="abs waste-bg" role="img" aria-label="Faded heap of mixed plastic waste"></div>
  <div class="abs num num-orange">01</div>
  <h3 class="abs sec-title" style="left:228px">Current<br>Challenges</h3>
  <div class="abs num num-green">02</div>
  <h3 class="abs sec-title" style="left:790px">Our<br>Solution!</h3>

  <div class="abs challenge" style="top:2414px">
    <svg width="36" height="44" viewBox="0 0 36 44"><path d="M8 3h20M8 41h20M10 3c0 12 16 12 16 19S10 29 10 41M26 3c0 12-16 12-16 19s16 7 16 19" fill="none" stroke="#e8652a" stroke-width="2"/></svg>
    <p>Today polymers are the dominating materials for most application in modern life. Global demand for polymers will double within the next 30 years</p>
  </div>
  <div class="abs challenge" style="top:2498px">
    <svg width="36" height="40" viewBox="0 0 36 40"><path d="M12 8l6-5 6 5M8 30l-5-8 6-4M28 30l5-8-6-4M18 3v10M3 22l10 8M33 22l-10 8" fill="none" stroke="#e8652a" stroke-width="2"/></svg>
    <p>Compounds, additives, colorants and contaminants put the limits to the recycling of polymers. More than 50% of all polymer waste is rejected and incinerated</p>
  </div>
  <div class="abs challenge" style="top:2582px">
    <svg width="36" height="40" viewBox="0 0 36 40"><path d="M2 38h32V20l-8 5v-5l-8 5v-5l-8 5V6H6v32" fill="none" stroke="#e8652a" stroke-width="2"/></svg>
    <p>Our industry is failing to meet the sustainability goals<br>set by the EU.</p>
  </div>

  <div class="abs solution" style="top:2414px">
    <h4>Advanced Recycling via Vendrafel Technology!</h4>
    <p>VENDRAFEL'S advanced depolymerisation technology allows the regeneration of a high quality liquid resource suitable for the production of new virgin quality polymers. It is applicable to mixed and contaminated plastics and of high efficiency.</p>
  </div>
  <a class="abs btn sol-btn">Learn more</a>

  <div class="abs video-small" role="img" aria-label="Video: shredded plastic in the recycling factory"><span class="play"></span></div>

  <svg class="abs" style="left:0;top:3100px" width="1200" height="140" viewBox="0 0 1200 140">
    <path d="M0 125 C300 40 480 20 600 20 C760 20 980 60 1200 125 L1200 140 L0 140 Z" fill="#fff"/>
  </svg>
  <div class="abs" style="left:0;top:3239px;width:1200px;height:540px;background:#fff"></div>

  <!-- how it works -->
  <h2 class="abs how-title">How Does it work?</h2>
  <svg class="abs" style="left:420px;top:3300px" width="360" height="360" viewBox="0 0 360 360">
    <circle cx="180" cy="180" r="165" fill="none" stroke="#e8652a" stroke-width="2" stroke-dasharray="700 40 300 40"/>
    <circle cx="180" cy="180" r="120" fill="none" stroke="#f2a324" stroke-width="18" opacity=".25"/>
    <path d="M320 95l10 -8 2 14" fill="none" stroke="#e8652a" stroke-width="2"/>
    <path d="M40 265l-10 8 -2 -14" fill="none" stroke="#e8652a" stroke-width="2"/>
  </svg>
  <p class="abs step" style="left:230px;top:3322px;width:168px;text-align:right">A plastic product is produced and used by individua customers</p>
  <svg class="abs" style="left:438px;top:3325px" width="42" height="48" viewBox="0 0 42 48"><rect x="6" y="10" width="16" height="34" rx="3" fill="none" stroke="#e8652a" stroke-width="2"/><path d="M10 4h8v6h-8z" fill="none" stroke="#e8652a" stroke-width="2"/><circle cx="30" cy="36" r="8" fill="none" stroke="#e8652a" stroke-width="2"/></svg>
  <svg class="abs" style="left:756px;top:3372px" width="52" height="46" viewBox="0 0 52 46"><path d="M2 44h48V26l-10 6v-6l-10 6v-6l-10 6V8h-8v36" fill="none" stroke="#e8652a" stroke-width="2"/></svg>
  <p class="abs step" style="left:835px;top:3382px;width:180px">The recycled oils are handled by the plastic product producer</p>
  <svg class="abs" style="left:428px;top:3570px" width="40" height="48" viewBox="0 0 40 48"><path d="M4 10h32M14 10V4h12v6M8 10l3 34h18l3-34M16 18v20M24 18v20" fill="none" stroke="#e8652a" stroke-width="2"/></svg>
  <p class="abs step" style="left:230px;top:3573px;width:156px;text-align:right">After being used, the product is being disposed off</p>
  <svg class="abs" style="left:695px;top:3600px" width="56" height="52" viewBox="0 0 56 52"><path d="M22 8l6-6 6 6M10 40l-7-10 8-4M46 40l7-10-8-4M28 2v14M3 30l14 10M53 30l-14 10" fill="none" stroke="#e8652a" stroke-width="2"/></svg>
  <div class="abs step" style="left:786px;top:3580px;width:230px">
    <div class="brand-sm">vendrafel</div>
    The waste is collected and processed via Vendrafel's advanced recycling technology
  </div>

  <!-- products -->
  <div class="abs products" role="img" aria-label="Faded seashore covered with plastic waste"></div>
  <h2 class="abs products-title">Our products</h2>
  <div class="abs product" style="left:206px">
    <div class="thumb" style="background:#7d7d7d"><div class="wordmark" style="color:#9a9a9a">vendrafel</div></div>
    <h5>Product Name</h5>
    <p>A plastic product is produced and used by individua customers</p>
  </div>
  <div class="abs product" style="left:622px">
    <div class="thumb" style="background:#ececec"><div class="wordmark">vendrafel</div><span style="font-size:13px;color:#aaa">Product Image</span></div>
    <h5>Product Name</h5>
    <p>A plastic product is produced and used by individua customers</p>
  </div>

  <!-- footer -->
  <footer class="abs footer"></footer>
  <div class="abs f-brand"><div class="wordmark" style="color:#8a8a8a">vendrafel</div></div>
  <div class="abs f-h" style="left:162px;top:4486px">CONTACT US</div>
  <svg class="abs" style="left:162px;top:4530px" width="14" height="18" viewBox="0 0 14 18"><path d="M7 17S1 10 1 6.5a6 6 0 0 1 12 0C13 10 7 17 7 17z" fill="#fff"/><circle cx="7" cy="6.5" r="2" fill="#353535"/></svg>
  <p class="abs f-text" style="left:192px;top:4528px;width:200px">312/ Lorem Ipsum is simply dummy text of the printing</p>
  <svg class="abs" style="left:162px;top:4586px" width="16" height="16" viewBox="0 0 16 16"><path d="M3 1l3 3-2 2c1 2 3 4 5 5l2-2 3 3-2 3C7 14 2 9 1 3z" fill="#fff"/></svg>
  <p class="abs f-text" style="left:192px;top:4584px;font-size:14px">555 0142 770</p>

  <div class="abs f-h" style="left:508px;top:4402px">QUICK LINKS</div>
  <ul class="abs f-list" style="left:508px;top:4434px">
    <li>Home</li><li>Our Partners</li><li>Technology</li><li>System &amp; Operations</li><li>Contact Us</li><li>How its works</li>
  </ul>

  <div class="abs f-h" style="left:707px;top:4402px">SIGN UP FOR NEWSLETTER</div>
  <p class="abs f-text" style="left:707px;top:4436px;width:240px;font-size:12px">If you&nbsp; have any questions please send us a message.</p>
  <div class="abs newsletter"><span>Email address</span><span class="btn">Subscribe</span></div>

  <div class="abs f-rule"></div>
  <div class="abs social"><span></span><span></span><span></span><span></span></div>
  <p class="abs copy">© 2021 Vendrafel. All Rights are Reserved.</p>
</div>
</body>
</html>
```